Veltrano - Mechanic/Collision Center Business Card

We're looking for a business card design for our mechanic/ collision repair shop.

Can be with colours or monochromatic.

See the attached files.

Many thanks

```html
<!DOCTYPE html>
<html lang="pt">
<head>
<meta charset="utf-8">
<title>Veltrano – Business Card</title>
<link href="https://fonts.googleapis.com/css2?family=Outfit:wght@300;400;500;700&display=swap" rel="stylesheet">
<style>
  :root {
    --page: #ffffff;
    --card-light: #ffffff;
    --card-border: #d6d6d6;
    --card-dark: #1c1f21;
    --ink: #111417;
    --accent: #1a6fa0;
    --brand-blue: #229fdb;
    --ghost-light: #f2f5f9;
    --ghost-dark: #17191b;
    --white: #ffffff;
  }
  * { box-sizing: border-box; margin: 0; padding: 0; }
  html, body {
    width: 1200px; height: 1200px; overflow: hidden;
    background: var(--page);
    font-family: "Outfit", sans-serif;
    color: var(--ink);
  }
  .canvas { position: relative; width: 1200px; height: 1200px; }
  .card {
    position: absolute; left: 190px; width: 828px; height: 473px; overflow: hidden;
  }
  .card--front { top: 83px; background: var(--card-light); border: 1px solid var(--card-border); }
  .card--back { top: 651px; background: var(--card-dark); }

  .backdrop {
    position: absolute; left: 4px; right: 4px; top: 76px; height: 318px;
    border-radius: 60px 60px 14px 14px;
  }
  .card--front .backdrop { background: linear-gradient(180deg, rgba(242,245,249,0.35), var(--ghost-light) 40%); }
  .card--back .backdrop { background: linear-gradient(180deg, rgba(23,25,27,0.4), var(--ghost-dark) 40%); }

  .brand {
    position: absolute; left: 0; right: 0; display: flex; align-items: center; justify-content: center; gap: 8px;
    font-weight: 700; letter-spacing: 0.04em;
  }
  .brand__dot { border-radius: 50%; background: var(--brand-blue); }
  .card--front .brand { top: 88px; font-size: 24px; color: var(--ink); }
  .card--front .brand__dot { width: 14px; height: 14px; }
  .card--back .brand { top: 218px; font-size: 46px; color: var(--white); gap: 14px; }
  .card--back .brand__dot { width: 26px; height: 26px; }

  .company {
    position: absolute; left: 93px; top: 180px;
    font-size: 24px; font-weight: 500; line-height: 1;
  }
  .company__rule { position: absolute; left: 89px; top: 211px; width: 171px; height: 1px; background: var(--ink); }

  .contacts { position: absolute; left: 84px; top: 226px; list-style: none; }
  .contacts li { display: flex; align-items: center; height: 27px; font-size: 18px; line-height: 1; }
  .contacts li svg { width: 24px; height: 24px; margin-right: 9px; flex: none; }

  .divider { position: absolute; left: 413px; top: 196px; width: 1px; height: 165px; background: var(--ink); }

  .person { position: absolute; left: 461px; top: 222px; }
  .person__name { font-size: 40px; font-weight: 300; line-height: 1; letter-spacing: -0.01em; }
  .person__name strong { font-weight: 700; }
  .person__role { margin-top: 3px; font-size: 13px; letter-spacing: 0.62em; color: var(--accent); font-weight: 400; }
  .person__rule { position: absolute; left: 463px; top: 289px; width: 170px; height: 1px; background: var(--ink); }
  .person__phone { position: absolute; left: 462px; top: 302px; display: flex; align-items: center; font-size: 18px; }
  .person__phone svg { width: 24px; height: 24px; margin-right: 7px; }

  .icon-ring { fill: none; stroke: var(--accent); stroke-width: 1.2; }
  .icon-fill { fill: var(--accent); }
  .icon-line { fill: none; stroke: var(--accent); stroke-width: 1.4; stroke-linejoin: round; }
</style>
</head>
<body>
<div class="canvas">

  <section class="card card--front">
    <div class="backdrop" role="img" aria-label="Faint silhouettes of three cars behind the card content"></div>

    <div class="brand"><span class="brand__dot"></span><span>VELTRANO</span></div>

    <h1 class="company">Veltrano, LDA</h1>
    <div class="company__rule"></div>

    <ul class="contacts">
      <li>
        <svg viewBox="0 0 24 24"><circle class="icon-ring" cx="12" cy="12" r="11"/><path class="icon-line" d="M12 18.5c-3-3.6-4.5-6-4.5-8a4.5 4.5 0 0 1 9 0c0 2-1.5 4.4-4.5 8z"/><circle class="icon-line" cx="12" cy="10.4" r="1.6"/></svg>
        Rua do Carmo Velho, 42
      </li>
      <li>
        <svg viewBox="0 0 24 24"><circle class="icon-ring" cx="12" cy="12" r="11"/><path class="icon-fill" d="M6.5 11 12 6.5l5.5 4.5V17h-11z"/></svg>
        4000-117 Porto
      </li>
      <li>
        <svg viewBox="0 0 24 24"><circle class="icon-ring" cx="12" cy="12" r="11"/><path class="icon-fill" d="M8.6 6.8l1.7-.3 1.2 2.8-1.2 1a7 7 0 0 0 3.4 3.4l1-1.2 2.8 1.2-.3 1.7c-.2.6-.8 1-1.5.9-4.2-.6-7.5-3.9-8.1-8.1-.1-.7.3-1.3 1-1.4z"/></svg>
        +351 213402518
      </li>
      <li>
        <svg viewBox="0 0 24 24"><circle class="icon-ring" cx="12" cy="12" r="11"/><rect class="icon-fill" x="6.5" y="8" width="11" height="8" rx="1"/><path d="M7 8.8l5 3.8 5-3.8" fill="none" stroke="#fff" stroke-width="1.1"/></svg>
        veltrano.mail@exemplo.pt
      </li>
      <li>
        <svg viewBox="0 0 24 24"><circle class="icon-ring" cx="12" cy="12" r="11"/></svg>
        www.social.example/veltrano
      </li>
    </ul>

    <div class="divider"></div>

    <div class="person">
      <h2 class="person__name">Rui <strong>Marques</strong></h2>
      <p class="person__role">MANAGER</p>
    </div>
    <div class="person__rule"></div>
    <div class="person__phone">
      <svg viewBox="0 0 24 24"><circle class="icon-ring" cx="12" cy="12" r="11"/><path class="icon-fill" d="M8.6 6.8l1.7-.3 1.2 2.8-1.2 1a7 7 0 0 0 3.4 3.4l1-1.2 2.8 1.2-.3 1.7c-.2.6-.8 1-1.5.9-4.2-.6-7.5-3.9-8.1-8.1-.1-.7.3-1.3 1-1.4z"/></svg>
      +351 912774306
    </div>
  </section>

  <section class="card card--back">
    <div class="backdrop" role="img" aria-label="Dark silhouettes of three cars behind the brand name"></div>
    <div class="brand"><span class="brand__dot"></span><span>VELTRANO</span></div>
  </section>

</div>
</body>
</html>
```